THE TALL COPPER ATLAS OF PORTS

subtitle: AN INTRO TO SEARCH ENGINE OPTIMIZATION
background: white
dimensions: 1562x2500

Target Market(s)

Marketing professionals

Industry/Entity Type

Digital Marketing

Font styles to use
Sans Serif

Colors
ffffff
1b1b1b
3176b5

Requirements
Should not have
• Images or graphics

```html
<!DOCTYPE html>
<html lang="en">
<head>
<meta charset="utf-8">
<title>The Tall Copper Atlas of Ports — Book Cover</title>
<link rel="stylesheet" href="https://fonts.googleapis.com/css2?family=Anton&family=Oswald:wght@400;500;700&display=swap">
<style>
  :root {
    --backdrop: #808185;
    --paper: #ffffff;
    --ink: #111111;
    --accent-blue: #0054a6;
  }
  html, body {
    margin: 0;
    padding: 0;
    width: 1200px;
    height: 1200px;
    overflow: hidden;
    background: var(--backdrop);
  }
  .book-cover {
    position: absolute;
    left: 240px;
    top: 22px;
    width: 720px;
    height: 1154px;
    background: var(--paper);
  }
  .book-cover svg {
    display: block;
    width: 720px;
    height: 1154px;
  }
  .title-small {
    font-family: "Oswald", sans-serif;
    font-weight: 500;
    fill: var(--ink);
  }
  .title-large {
    font-family: "Oswald", sans-serif;
    font-weight: 700;
    fill: var(--accent-blue);
  }
  .title-middle {
    font-family: "Oswald", sans-serif;
    font-weight: 400;
    fill: var(--ink);
    letter-spacing: 3px;
  }
  .title-hero {
    font-family: "Anton", sans-serif;
    fill: var(--accent-blue);
  }
  .subtitle {
    font-family: "Oswald", sans-serif;
    font-weight: 400;
    fill: var(--ink);
  }
  .author-name {
    font-family: "Oswald", sans-serif;
    font-weight: 500;
    fill: var(--accent-blue);
    letter-spacing: 14px;
  }
  .rule {
    stroke: var(--ink);
    stroke-width: 3;
  }
</style>
</head>
<body>
  <main class="book-cover">
    <svg viewBox="0 0 720 1154" xmlns="http://www.w3.org/2000/svg" aria-labelledby="cover-title">
      <title id="cover-title">The Tall Copper Atlas of Ports: An Intro to Search Engine Optimization</title>
      <g class="title-block" text-anchor="middle">
        <text class="title-small" x="360" y="100" font-size="66">THE</text>
        <text class="title-large" x="360" y="263" font-size="187">TALL</text>
        <text class="title-large" x="360" y="432" font-size="187" textLength="500" lengthAdjust="spacingAndGlyphs">COPPER</text>
        <text class="title-middle" x="360" y="560" font-size="102">ATLAS OF</text>
        <text class="title-hero" x="360" y="890" font-size="360" textLength="570" lengthAdjust="spacingAndGlyphs">PORTS</text>
      </g>

      <line class="rule" x1="100" y1="912" x2="621" y2="912"/>

      <g class="subtitle-block" text-anchor="middle">
        <text class="subtitle" x="360" y="966" font-size="51" textLength="440" lengthAdjust="spacingAndGlyphs">AN INTRO TO SEARCH</text>
        <text class="subtitle" x="360" y="1014" font-size="51" textLength="452" lengthAdjust="spacingAndGlyphs">ENGINE OPTIMIZATION</text>
      </g>

      <line class="rule" x1="100" y1="1027" x2="621" y2="1027"/>

      <text class="author-name" x="367" y="1100" font-size="46" text-anchor="middle">AUTHOR NAME</text>
    </svg>
  </main>
</body>
</html>
```